stationery
business cards, letterhead, and envelopes
Professional
Marisol Dunkerly
Mortgage Loan Originator / Owner
418 Kettering Avenue Ste 2270
Honolulu HI 96813
TideRiverCredit@quillmail.com
www.BrightCedarLending.com
Lowest Rates In Hawaii !!!!!

```html
<!DOCTYPE html>
<html lang="en">
<head>
<meta charset="utf-8">
<title>Bright Cedar Lending — Stationery</title>
<link href="https://fonts.googleapis.com/css2?family=Lato:wght@400;700&display=swap" rel="stylesheet">
<style>
:root{
  --bg:#ece4d6;
  --paper:#ffffff;
  --navy:#2b3a8f;
  --blue:#3f56b8;
  --grey:#8e9096;
  --grey-dark:#5e6066;
  --ink:#4a4a4a;
  --label:#6b5e4c;
  --faint:#f1ebdf;
}
*{box-sizing:border-box;margin:0;padding:0}
html,body{width:1200px;height:446px;overflow:hidden;background:var(--bg);font-family:"Lato",Arial,sans-serif;color:var(--ink)}
.board{position:relative;width:1200px;height:446px}
.label{position:absolute;font-size:7px;letter-spacing:1px;text-transform:uppercase;color:var(--label)}
.sheet{position:absolute;background:var(--paper);box-shadow:0 2px 5px rgba(0,0,0,.18);overflow:hidden}
.swoosh{position:absolute;top:0;right:0}
.brand{display:flex;align-items:center;gap:4px;color:var(--navy);font-weight:700;white-space:nowrap}
.brand-dot{border-radius:50%;background:var(--navy)}
.watermark{position:absolute;border-radius:50%;background:var(--faint)}
.contact{position:absolute;font-size:5px;line-height:7px;color:var(--grey-dark)}
.card-front .brand{font-size:6px}
.letterhead .brand{position:absolute;top:16px;left:50%;transform:translateX(-50%);font-size:11px}
.letterhead .brand-dot{width:8px;height:8px}
.envelope-front .brand{position:absolute;top:20px;left:16px;font-size:13px}
.envelope-front .brand-dot{width:10px;height:10px}
.tagline{font-size:5px;color:var(--grey-dark)}
</style>
</head>
<body>
<main class="board">
  <span class="label" style="left:19px;top:112px">Stationery Concepts</span>

  <!-- Business card front -->
  <section class="sheet card-front" style="left:19px;top:151px;width:125px;height:43px">
    <svg class="swoosh" width="60" height="14" viewBox="0 0 60 14"><path d="M0 0H60V14C40 4 20 2 0 0Z" fill="var(--grey)"/><path d="M8 0H60V10C42 3 26 1 8 0Z" fill="var(--blue)"/></svg>
    <div class="brand" style="position:absolute;left:6px;top:16px"><span class="brand-dot" style="width:5px;height:5px"></span>Bright Cedar Lending</div>
    <p class="contact" style="left:6px;top:26px;font-size:4px;line-height:5px">Marisol Dunkerly · Loan Originator<br>808 555 0142</p>
  </section>
  <span class="label" style="left:19px;top:200px">Business Card Front</span>

  <!-- Business card back -->
  <section class="sheet card-back" style="left:19px;top:247px;width:125px;height:41px">
    <svg class="swoosh" width="60" height="14" viewBox="0 0 60 14"><path d="M0 0H60V14C40 4 20 2 0 0Z" fill="var(--grey)"/><path d="M8 0H60V10C42 3 26 1 8 0Z" fill="var(--blue)"/></svg>
    <div class="brand" style="position:absolute;left:8px;top:18px;font-size:7px"><span class="brand-dot" style="width:6px;height:6px"></span>Bright Cedar Lending</div>
  </section>
  <span class="label" style="left:19px;top:294px">Business Card Back</span>

  <!-- Letterhead option 1 -->
  <section class="sheet letterhead" style="left:151px;top:12px;width:319px;height:338px">
    <svg class="swoosh" width="150" height="38" viewBox="0 0 150 38"><path d="M0 0H150V38C110 14 60 4 0 0Z" fill="var(--grey)"/><path d="M20 0H150V30C114 10 70 3 20 0Z" fill="var(--blue)"/></svg>
    <div class="brand"><span class="brand-dot"></span>Bright Cedar Lending</div>
    <div class="watermark" style="left:112px;top:130px;width:95px;height:95px"></div>
    <p class="contact" style="left:16px;top:298px">808 555 0142<br>TideRiverCredit@quillmail.com<br>www.BrightCedarLending.com<br>418 Kettering Avenue Ste 2270</p>
  </section>
  <span class="label" style="left:280px;top:356px">Letter Head Option 1</span>

  <!-- Letterhead option 2 -->
  <section class="sheet letterhead" style="left:481px;top:12px;width:319px;height:338px">
    <svg class="swoosh" width="150" height="38" viewBox="0 0 150 38"><path d="M0 0H150V38C110 14 60 4 0 0Z" fill="var(--grey)"/><path d="M20 0H150V30C114 10 70 3 20 0Z" fill="var(--blue)"/></svg>
    <div class="brand"><span class="brand-dot"></span>Bright Cedar Lending</div>
    <div class="watermark" style="left:112px;top:130px;width:95px;height:95px"></div>
    <p class="contact" style="left:0;right:0;top:318px;text-align:center">808 555 0142 · TideRiverCredit@quillmail.com · www.BrightCedarLending.com</p>
  </section>
  <span class="label" style="left:610px;top:356px">Letter Head Option 2</span>

  <!-- Envelope backs -->
  <svg class="sheet" style="left:842px;top:12px" width="318" height="60" viewBox="0 0 318 60">
    <rect width="318" height="60" fill="var(--blue)"/><rect y="46" width="318" height="14" fill="var(--paper)"/>
  </svg>
  <svg class="sheet" style="left:842px;top:86px" width="318" height="140" viewBox="0 0 318 140">
    <rect width="318" height="140" fill="var(--paper)"/>
    <path d="M0 0H318V40C300 60 250 72 200 72H118C68 72 18 60 0 40Z" fill="var(--grey-dark)"/>
    <path d="M0 60C18 92 68 104 118 104H200C250 104 300 92 318 60" fill="none" stroke="#d5d5d5"/>
    <circle cx="159" cy="95" r="9" fill="var(--navy)"/>
  </svg>

  <!-- Envelope front -->
  <section class="sheet envelope-front" style="left:800px;top:264px;width:357px;height:156px">
    <svg class="swoosh" width="170" height="44" viewBox="0 0 170 44"><path d="M0 0H170V44C126 16 70 4 0 0Z" fill="var(--grey)"/><path d="M24 0H170V34C130 12 80 3 24 0Z" fill="var(--blue)"/></svg>
    <div class="brand"><span class="brand-dot"></span>Bright Cedar Lending</div>
    <p class="tagline" style="position:absolute;left:30px;top:38px">Lowest Rates In Hawaii !!!!!</p>
  </section>
  <span class="label" style="left:960px;top:428px">Envelope Option 1</span>
</main>
</body>
</html>
```